Travel Consultant Business Card

Hello.. New travel consultant looking seeking a business card that incorporates my new logo. I specialize in cruises but also want to imply land vacation. I am very open to any design and font concepts. I'm looking for a very upbeat modern design that reflects cruise and land vacations. Bright vibrant colors

Target Market(s)

Cruise and Land Vacationers

Industry/Entity Type

Travel Agent

Contact Information for Business Card

I am very open to any design and font concepts. I'm looking for a very upbeat modern design that reflects cruise and land vacations. Bright vibrant colors

Colors

Designer to choose colors to be used in the design.

Requirements
Must have
• Company Name: PineRidge Journeys---New logo uploaded to be included in design
• My Name: Danielle Marchetti-Travel Consultant
• Phone Number: (555) 418-7093
• E-Mail Address: pineridgejourneys@mailbox-example.com
• Website: www.pineridgejourneys-example.com
Nice to have
• My tag line is …..Here to Get You There

```html
<!DOCTYPE html>
<html lang="en">
<head>
<meta charset="utf-8">
<title>PineRidge Journeys – Business Card</title>
<link rel="stylesheet" href="https://fonts.googleapis.com/css2?family=Roboto+Condensed:ital,wght@1,700&family=Work+Sans:wght@400;700&display=swap">
<style>
  :root {
    --stage: #3a3d42;
    --card-white: #ffffff;
    --card-shade: #eceef0;
    --brand-blue: #1656a8;
    --brand-deep: #0f4a91;
    --brand-light: #3a9bd8;
    --text-grey: #6b6f75;
    --back-name: #5bb3e6;
  }
  * { margin: 0; padding: 0; box-sizing: border-box; }
  html, body {
    width: 1200px; height: 900px; overflow: hidden;
    background: var(--stage);
  }
  .canvas {
    position: relative; width: 1200px; height: 900px;
    display: flex; flex-direction: column; align-items: center;
    justify-content: center; gap: 28px;
  }
  .card {
    position: relative; width: 700px; height: 400px;
    box-shadow: 0 10px 30px rgba(0,0,0,.45);
    overflow: hidden;
  }
  /* Front */
  .card-front {
    background: linear-gradient(135deg, var(--card-shade) 0%, var(--card-white) 45%, var(--card-white) 100%);
  }
  .name-block { position: absolute; left: 0; top: 62px; display: flex; }
  .name-marker {
    width: 26px; height: 36px; background: var(--brand-blue);
  }
  .name-text { margin-left: 16px; }
  .person-name {
    font-family: "Roboto Condensed", sans-serif; font-style: italic; font-weight: 700;
    font-size: 30px; letter-spacing: 1px; text-transform: uppercase;
    color: var(--brand-blue); line-height: 1;
  }
  .person-title {
    font-family: "Work Sans", sans-serif; font-weight: 400;
    font-size: 17px; color: var(--text-grey); margin-top: 6px;
  }
  .company-lockup {
    position: absolute; right: 44px; top: 150px;
    display: flex; align-items: center; gap: 12px;
  }
  .company-dot {
    width: 18px; height: 18px; border-radius: 50%; background: var(--brand-blue);
  }
  .company-name {
    font-family: "Work Sans", sans-serif; font-weight: 700;
    font-size: 32px; color: var(--brand-blue); white-space: nowrap;
  }
  .address {
    position: absolute; left: 330px; top: 228px;
    font-family: "Work Sans", sans-serif; font-size: 16px; line-height: 1.45;
    color: var(--text-grey);
  }
  .contact-list {
    position: absolute; left: 300px; top: 300px; list-style: none;
    font-family: "Work Sans", sans-serif; font-size: 15px; color: var(--text-grey);
  }
  .contact-list li { display: flex; align-items: center; gap: 10px; line-height: 1.6; }
  .contact-list svg { width: 13px; height: 13px; flex: none; }
  /* Back */
  .card-back {
    background: linear-gradient(135deg, var(--brand-blue) 0%, var(--brand-deep) 100%);
    display: flex; align-items: center; justify-content: center; gap: 18px;
  }
  .back-dot { width: 26px; height: 26px; border-radius: 50%; background: var(--back-name); }
  .back-name {
    font-family: "Work Sans", sans-serif; font-weight: 700;
    font-size: 52px; color: var(--back-name); white-space: nowrap;
  }
</style>
</head>
<body>
<main class="canvas">
  <section class="card card-front">
    <div class="name-block">
      <div class="name-marker"></div>
      <div class="name-text">
        <h1 class="person-name">Danielle Marchetti</h1>
        <p class="person-title">Travel Consultant</p>
      </div>
    </div>

    <div class="company-lockup">
      <span class="company-dot"></span>
      <span class="company-name">PineRidge Journeys</span>
    </div>

    <p class="address">214b Harbour Lane,<br>Lakeview, NZ, 4021</p>

    <ul class="contact-list">
      <li>
        <svg viewBox="0 0 16 16" aria-hidden="true"><path fill="#1656a8" d="M4 1l2.5 3-1.5 2c1 2 2.5 3.5 4.5 4.5l2-1.5 3 2.5-1.5 2.5C7 15 1 9 1.5 2.5z"/></svg>
        (555) 418-7093
      </li>
      <li>
        <svg viewBox="0 0 16 16" aria-hidden="true"><rect x="1" y="3" width="14" height="10" rx="1" fill="none" stroke="#1656a8" stroke-width="1.6"/><path d="M1.5 4l6.5 5 6.5-5" fill="none" stroke="#1656a8" stroke-width="1.6"/></svg>
        pineridgejourneys@mailbox-example.com
      </li>
      <li>
        <svg viewBox="0 0 16 16" aria-hidden="true"><circle cx="8" cy="8" r="6.5" fill="none" stroke="#1656a8" stroke-width="1.5"/><ellipse cx="8" cy="8" rx="2.8" ry="6.5" fill="none" stroke="#1656a8" stroke-width="1.2"/><path d="M1.5 8h13" stroke="#1656a8" stroke-width="1.2"/></svg>
        www.pineridgejourneys-example.com
      </li>
    </ul>
  </section>

  <section class="card card-back">
    <span class="back-dot"></span>
    <span class="back-name">PineRidge Journeys</span>
  </section>
</main>
</body>
</html>
```